Pictures required on web page

I would like change three existing pictures on my new website.

The site can be found here:
http://mossbottleroom.kestrelweb.com.au/

The three pictures to be changed are on the home page:
Purchase- Mixed Packs
Wine Club - Let Us Choose
Education- Wine Courses

I would like somthing stylish, classic and understated that fits in with the theme and feel of the site. I know stylish is a subjective thing. At the moment, the current picture makes the text difficult to read on a destop. Plus I don't think they are a perfect fit for our website anyway. I've attached a photo of our wine course room and also me in the store. Please, don't feel as though you have to use these pictures, but they're there if you want them. However I'm open to completely different photos/graphics to be used.

```html
<!DOCTYPE html>
<html lang="en">
<head>
<meta charset="utf-8">
<title>Vinehollow — Small winery specialist</title>
<link rel="stylesheet" href="https://fonts.googleapis.com/css2?family=Roboto:wght@400;500&family=Roboto+Slab:wght@300;400;700&display=swap">
<style>
  :root {
    --header-top: #2b3b60;
    --header-bottom: #1f2c4b;
    --nav-bar: #151c2b;
    --page: #ffffff;
    --ink-light: #ffffff;
    --ink-soft: #cfd6e6;
    --search-bg: #34456d;
    --search-line: #6a7aa0;
    --divider: #46557a;
    --tile-shade: #2a2f44;
    --tile-deep: #1c2236;
    --shipping: #b34745;
    --newsletter: #1f2c4b;
    --frame: rgba(255,255,255,0.75);
  }
  * { box-sizing: border-box; margin: 0; padding: 0; }
  html, body { width: 1200px; height: 618px; overflow: hidden; background: var(--page); }
  body { position: relative; font-family: "Roboto", Arial, sans-serif; color: var(--ink-light); }

  .site-header {
    position: absolute; left: 0; top: 0; width: 1200px; height: 114px;
    background: linear-gradient(180deg, var(--header-top), var(--header-bottom));
  }
  .brand { position: absolute; left: 62px; top: 24px; }
  .brand-name { font-family: "Roboto Slab", Georgia, serif; font-weight: 700; font-size: 37px; line-height: 1; }
  .brand-tagline { font-family: "Roboto Slab", Georgia, serif; font-weight: 300; font-size: 18px; margin-top: 6px; color: var(--ink-soft); }

  .search {
    position: absolute; left: 364px; top: 38px; width: 314px; height: 37px;
    background: var(--search-bg); border: 1px solid var(--search-line); border-radius: 3px;
    display: flex; align-items: center; padding-left: 13px;
    font-size: 16px; color: #a9b4cc;
  }
  .search svg { position: absolute; right: 10px; top: 7px; }

  .utility-nav { position: absolute; left: 711px; top: 30px; display: flex; }
  .utility-link {
    width: 86px; height: 46px; display: flex; flex-direction: column; align-items: center; justify-content: space-between;
    font-size: 13px; letter-spacing: 0.2px; color: var(--ink-soft); border-left: 1px solid var(--divider);
  }
  .utility-link:first-child { border-left: none; }

  .category-nav {
    position: absolute; left: 0; top: 114px; width: 1200px; height: 52px;
    background: var(--nav-bar); font-size: 19px;
  }
  .category-nav span { position: absolute; top: 14px; white-space: nowrap; }
  .cart { position: absolute; left: 967px; top: 12px; display: flex; align-items: center; gap: 8px; font-size: 14px; }

  .tile { position: absolute; overflow: hidden; text-align: center; }
  .tile-photo { position: absolute; inset: 0; }
  .tile-frame { position: absolute; border: 1px solid var(--frame); }
  .tile-kicker { position: absolute; left: 0; right: 0; font-family: "Roboto Slab", Georgia, serif; font-size: 16px; letter-spacing: 2.5px; }
  .tile-title { position: absolute; left: 0; right: 0; font-weight: 500; font-size: 29px; letter-spacing: 1.6px; }
  .tile-note { position: absolute; left: 0; right: 0; font-size: 15px; letter-spacing: 1.2px; }

  .courses { left: 40px; top: 182px; width: 355px; height: 237px; }
  .club { left: 416px; top: 182px; width: 356px; height: 410px; }
  .packs { left: 793px; top: 181px; width: 355px; height: 236px; }
  .shipping { left: 40px; top: 436px; width: 355px; height: 159px; background: var(--shipping); }
  .newsletter { left: 793px; top: 433px; width: 355px; height: 159px; background: var(--newsletter); }

  .photo-cellar {
    background: radial-gradient(ellipse at 50% 40%, #4a4650 0%, var(--tile-shade) 55%, var(--tile-deep) 100%);
  }
  .photo-cellar-tall {
    background: linear-gradient(180deg, #3a3a48 0%, var(--tile-shade) 45%, #3b3134 80%, var(--tile-deep) 100%);
  }
  .read-more {
    position: absolute; left: 102px; top: 242px; width: 152px; height: 39px;
    border: 1px solid var(--ink-light); font-family: "Roboto Slab", Georgia, serif; font-size: 16px;
    letter-spacing: 1.2px; line-height: 37px;
  }
  .shipping .tile-frame, .newsletter .tile-frame { border-color: rgba(255,255,255,0.35); }
</style>
</head>
<body>
  <header class="site-header">
    <div class="brand">
      <div class="brand-name">Vinehollow</div>
      <div class="brand-tagline">Small winery specialist.</div>
    </div>

    <div class="search">Search the Cellars
      <svg width="24" height="24" viewBox="0 0 24 24" fill="none" stroke="#e6ebf5" stroke-width="2.2">
        <circle cx="10" cy="10" r="7"/><line x1="15" y1="15" x2="22" y2="22"/>
      </svg>
    </div>

    <nav class="utility-nav">
      <div class="utility-link">
        <svg width="18" height="16" viewBox="0 0 18 16" fill="#c9d2e6"><path d="M9 1 L1 8 H3.5 V15 H7.5 V10.5 H10.5 V15 H14.5 V8 H17 Z"/></svg>HOME</div>
      <div class="utility-link">
        <svg width="22" height="16" viewBox="0 0 22 16" fill="#c9d2e6"><circle cx="11" cy="4" r="3.2"/><circle cx="4.5" cy="5" r="2.4"/><circle cx="17.5" cy="5" r="2.4"/><path d="M5.5 16 C5.5 10 16.5 10 16.5 16 Z"/><path d="M0 14 C0 9 6 8.5 7 10 L5 14 Z"/><path d="M22 14 C22 9 16 8.5 15 10 L17 14 Z"/></svg>ABOUT</div>
      <div class="utility-link">
        <svg width="17" height="17" viewBox="0 0 17 17" fill="none" stroke="#c9d2e6" stroke-width="1.6"><rect x="1" y="3" width="15" height="13"/><line x1="1" y1="7" x2="16" y2="7"/><line x1="5" y1="0.5" x2="5" y2="4.5"/><line x1="12" y1="0.5" x2="12" y2="4.5"/></svg>EVENTS</div>
      <div class="utility-link">
        <svg width="17" height="17" viewBox="0 0 17 17"><circle cx="8.5" cy="8.5" r="5.5" fill="none" stroke="#c9d2e6" stroke-width="3.5" stroke-dasharray="2.6 1.7"/><circle cx="8.5" cy="8.5" r="4.5" fill="#c9d2e6"/><circle cx="8.5" cy="8.5" r="2" fill="#26355a"/></svg>ACCOUNT</div>
      <div class="utility-link">
        <svg width="15" height="16" viewBox="0 0 15 16" fill="#c9d2e6"><path d="M3 1 L6 4.5 L4.5 6.5 C5.5 9 7 10.5 9 11.5 L11 10 L14.5 13 L12.5 15.5 C6 15 0.5 9 0.8 3 Z"/></svg>CONTACT</div>
    </nav>
  </header>

  <nav class="category-nav">
    <span style="left:62px">Red Wine</span>
    <span style="left:177px">White Wine</span>
    <span style="left:309px">Sparkling</span>
    <span style="left:424px">Rosé</span>
    <span style="left:500px">Old &amp; Rare</span>
    <span style="left:624px">Stickies</span>
    <span style="left:726px">Imported</span>
    <span style="left:838px">Wine Club</span>
    <div class="cart">
      <svg width="24" height="22" viewBox="0 0 24 22" fill="#ffffff"><path d="M0 1 H4 L5 4 H23 L20.5 13 H7.5 L8.2 15 H20 V17 H6.8 L3 3 H0 Z"/><circle cx="9" cy="19.5" r="2"/><circle cx="18" cy="19.5" r="2"/></svg>
      Shopping cart is empty
    </div>
  </nav>

  <main>
    <a class="tile courses">
      <div class="tile-photo photo-cellar" role="img" aria-label="Dim wine cellar with shelves of bottles and a tasting table"></div>
      <div class="tile-frame" style="left:24px;top:22px;width:307px;height:193px"></div>
      <div class="tile-kicker" style="top:84px">EDUCATION</div>
      <div class="tile-title" style="top:114px">WINE COURSES</div>
    </a>

    <a class="tile club">
      <div class="tile-photo photo-cellar-tall" role="img" aria-label="Wine course room with bottle-lined shelves and chairs"></div>
      <div class="tile-frame" style="left:25px;top:22px;width:307px;height:366px"></div>
      <div class="tile-kicker" style="top:130px">WINE CLUB</div>
      <div class="tile-title" style="top:161px">LET US CHOOSE</div>
      <div class="read-more">READ MORE</div>
    </a>

    <a class="tile packs">
      <div class="tile-photo photo-cellar" role="img" aria-label="Wine store shelves stocked with bottles"></div>
      <div class="tile-frame" style="left:21px;top:22px;width:309px;height:193px"></div>
      <div class="tile-kicker" style="top:84px">PURCHASE</div>
      <div class="tile-title" style="top:113px">MIXED PACKS</div>
    </a>

    <a class="tile shipping">
      <div class="tile-frame" style="left:22px;top:22px;width:311px;height:115px"></div>
      <div class="tile-title" style="top:54px;font-size:21px;font-weight:400;letter-spacing:2.2px">FREE SHIPPING</div>
      <div class="tile-note" style="top:85px">on orders over $200</div>
    </a>

    <a class="tile newsletter">
      <div class="tile-frame" style="left:21px;top:23px;width:310px;height:111px"></div>
      <div class="tile-title" style="top:55px;font-size:21px;font-weight:400;letter-spacing:2.2px">NEWSLETTER</div>
      <div class="tile-note" style="top:86px">join the newsletter for specials</div>
    </a>
  </main>
</body>
</html>
```